Life Coach for Lawyers Business Card Design

Elegant, original, business card design for life coaching service for associate attorneys who work in big law and struggle with stress, overwhelm, and time management. Double sided design.

Target Market(s)

Women associate attorneys who work in big law and struggle with stress, overwhelm, and time management.

Industry/Entity Type

Life Coaching

Contact Information for Business Card

Marissa Pendrell
Life Coach
518.677.3941
calmbriefcounsel.net
marissa@calmbriefcounsel.net
@calmbriefcounsel (Instagram)

Font styles to use
Other font styles liked:
• Silver South font duo. See uploaded files.

Requirements
Must have
• Icons for phone, website, email, and Instagram instead of words. Specific colors used in my logo (171B2B, 421121, FFFFFF)
Nice to have
• Foil. Embossed. Feminine design.
Should not have
• Any colors other than those used in logo. See uploaded files.

```html
<!DOCTYPE html>
<html lang="en">
<head>
<meta charset="utf-8">
<title>Calm Brief Counsel — Business Card</title>
<link href="https://fonts.googleapis.com/css2?family=Playfair+Display:wght@400&family=Cormorant+Garamond:wght@400;500&display=swap" rel="stylesheet">
<style>
  :root {
    --navy: #171B2B;
    --burgundy: #421121;
    --white: #FFFFFF;
    --rule: #1E2B36;
    --backdrop: #E9E9E6;
  }
  * { margin: 0; padding: 0; box-sizing: border-box; }
  html, body { width: 1200px; height: 1200px; overflow: hidden; background: var(--backdrop); }
  .stage { position: relative; width: 1200px; height: 1200px; }

  .card { position: absolute; overflow: hidden; box-shadow: 0 6px 18px rgba(0,0,0,.12); }

  /* Front (portrait) */
  .card--front { left: 70px; top: 250px; width: 400px; height: 700px; background: var(--white); }
  .front__brand {
    position: absolute; left: 0; right: 0; top: 150px; text-align: center;
    font-family: "Playfair Display", serif; font-weight: 400; color: var(--burgundy);
    font-size: 34px; line-height: 1.15; letter-spacing: 2px;
  }
  .front__panel { position: absolute; left: 0; top: 400px; width: 400px; height: 300px; background: var(--navy); }
  .front__band { position: absolute; left: 0; top: 90px; width: 400px; height: 110px; background: var(--burgundy); }
  .front__tab { position: absolute; left: 0; top: 0; }
  .front__name {
    position: absolute; left: 110px; top: 26px;
    font-family: "Playfair Display", serif; color: var(--white); font-size: 19px; letter-spacing: 1.5px;
  }
  .front__role {
    position: absolute; left: 110px; top: 52px;
    font-family: "Cormorant Garamond", serif; color: var(--white); font-size: 12px; letter-spacing: 2px;
  }
  .icon-chip { position: absolute; display: block; }
  .contact {
    position: absolute; left: 110px; font-family: "Cormorant Garamond", serif;
    color: var(--white); font-size: 15px; line-height: 1.35;
  }
  .contact--phone { top: 104px; }
  .contact--mail { top: 150px; }
  .front__social {
    position: absolute; right: 62px; top: 252px;
    font-family: "Cormorant Garamond", serif; color: var(--white); font-size: 15px;
  }

  /* Back (landscape) */
  .card--back { left: 540px; top: 420px; width: 600px; height: 343px; background: var(--navy); }
  .back__brand {
    position: absolute; left: 0; right: 0; top: 80px; text-align: center;
    font-family: "Playfair Display", serif; font-weight: 400; color: var(--white);
    font-size: 46px; line-height: 1.1; letter-spacing: 3px;
  }
  .back__rule { position: absolute; left: 0; top: 248px; width: 600px; height: 6px; background: var(--rule); }
  .back__band {
    position: absolute; left: 0; top: 254px; width: 600px; height: 89px; background: var(--burgundy);
    display: flex; align-items: center; justify-content: center; gap: 10px;
    font-family: "Cormorant Garamond", serif; color: var(--white); font-size: 17px; letter-spacing: .5px;
  }
</style>
</head>
<body>
<main class="stage">

  <section class="card card--front" aria-label="Business card front">
    <div class="front__brand">CALM BRIEF<br>COUNSEL</div>

    <div class="front__panel">
      <div class="front__band"></div>
      <svg class="front__tab" width="90" height="200" viewBox="0 0 90 200" aria-hidden="true">
        <polygon points="0,48 70,48 90,64 90,200 0,200" fill="#421121"/>
        <!-- phone -->
        <rect x="30" y="90" width="28" height="28" rx="5" fill="#FFFFFF"/>
        <path d="M38 96c2 0 3 4 2 5l-1 1c1 3 3 5 6 6l1-1c1-1 5 0 5 2l-1 3c-7 1-15-7-14-14z" fill="#421121"/>
        <!-- email / web -->
        <rect x="30" y="140" width="28" height="28" rx="5" fill="#FFFFFF"/>
        <rect x="36" y="147" width="16" height="11" rx="1" fill="none" stroke="#421121" stroke-width="2"/>
        <rect x="34" y="160" width="20" height="2.5" fill="#421121"/>
      </svg>

      <div class="front__name">MARISSA PENDRELL</div>
      <div class="front__role">LIFE COACH</div>
      <svg class="icon-chip" style="left:350px;top:28px" width="24" height="24" viewBox="0 0 24 24" aria-hidden="true">
        <rect width="24" height="24" rx="4" fill="#421121"/>
        <circle cx="12" cy="9" r="4" fill="#FFFFFF"/>
        <path d="M5 20c0-4 3-6 7-6s7 2 7 6z" fill="#FFFFFF"/>
      </svg>

      <div class="contact contact--phone">518.677.3941</div>
      <div class="contact contact--mail">marissa@calmbriefcounsel.net<br>calmbriefcounsel.net</div>

      <div class="front__social">@calmbriefcounsel</div>
      <svg class="icon-chip" style="left:350px;top:252px" width="22" height="22" viewBox="0 0 22 22" aria-hidden="true">
        <rect width="22" height="22" rx="4" fill="#421121"/>
      </svg>
    </div>
  </section>

  <section class="card card--back" aria-label="Business card back">
    <div class="back__brand">CALM BRIEF<br>COUNSEL</div>
    <div class="back__rule"></div>
    <div class="back__band">
      <svg width="20" height="20" viewBox="0 0 20 20" aria-hidden="true">
        <g fill="none" stroke="#FFFFFF" stroke-width="1.3">
          <circle cx="10" cy="10" r="8.5"/>
          <ellipse cx="10" cy="10" rx="4" ry="8.5"/>
          <line x1="1.5" y1="10" x2="18.5" y2="10"/>
          <line x1="3" y1="5.5" x2="17" y2="5.5"/>
          <line x1="3" y1="14.5" x2="17" y2="14.5"/>
        </g>
      </svg>
      <span>calmbriefcounsel.net</span>
    </div>
  </section>

</main>
</body>
</html>
```